Gobal construction supply company needs new business card design

I need a business card design for my global supply company using an existing logo. i will be looking to print these on rounded corner cards with the black background version of my logo on the back. on the front white background, my logo again and my simple details.

```html
<!DOCTYPE html>
<html lang="en">
<head>
<meta charset="utf-8">
<title>Meridian Civil Supply – Business Cards</title>
<link rel="stylesheet" href="https://fonts.googleapis.com/css2?family=Montserrat:wght@400;500;700;800&display=swap">
<style>
  :root {
    --backdrop: #5a5b5e;
    --card-white: #ffffff;
    --card-black: #111111;
    --ink-black: #141414;
    --ink-white: #f4f4f4;
    --brand-red: #d40000;
    --stripe-grey: #d9d9d9;
  }
  * { box-sizing: border-box; margin: 0; padding: 0; }
  html, body {
    width: 1200px;
    height: 1000px;
    overflow: hidden;
    background: var(--backdrop);
    font-family: "Montserrat", sans-serif;
  }
  .card {
    position: absolute;
    left: 220px;
    width: 760px;
    height: 434px;
    border-radius: 28px;
    overflow: hidden;
  }

  /* Front: logo side */
  .card--front {
    top: 44px;
    background: var(--card-white);
    display: flex;
    align-items: center;
    justify-content: center;
  }
  .brand__name {
    font-weight: 800;
    text-transform: uppercase;
    line-height: 1.1;
    letter-spacing: 0.5px;
    text-align: center;
  }
  .card--front .brand__name { color: var(--ink-black); font-size: 44px; }

  /* Back: details side */
  .card--back {
    top: 522px;
    background: radial-gradient(ellipse at 40% 30%, #262626 0%, var(--card-black) 70%);
  }
  .card--back .brand {
    position: absolute;
    left: 30px;
    top: 0;
    width: 340px;
    height: 300px;
    display: flex;
    align-items: center;
    justify-content: center;
  }
  .card--back .brand__name { color: var(--ink-white); font-size: 27px; }

  .divider {
    position: absolute;
    left: 392px;
    top: 84px;
    width: 2px;
    height: 196px;
    background: var(--brand-red);
  }
  .contact {
    position: absolute;
    left: 418px;
    top: 84px;
    color: var(--ink-white);
  }
  .contact__name {
    color: var(--brand-red);
    font-weight: 700;
    font-size: 21px;
    text-transform: uppercase;
  }
  .contact__title {
    font-size: 14px;
    font-weight: 400;
    margin-bottom: 16px;
  }
  .contact__address {
    font-size: 15.5px;
    font-weight: 500;
    line-height: 1.3;
    margin-bottom: 6px;
  }
  .contact__line {
    display: flex;
    align-items: center;
    gap: 9px;
    font-size: 16px;
    font-weight: 500;
    line-height: 1.5;
  }
  .contact__icon { width: 14px; height: 14px; flex: none; fill: var(--brand-red); }

  .wave {
    position: absolute;
    left: 0;
    bottom: 0;
    width: 760px;
    height: 434px;
  }
  .wave__stripe { fill: var(--stripe-grey); }
  .wave__band { fill: var(--brand-red); }
  .wave__gap { fill: var(--card-black); }
</style>
</head>
<body>

<section class="card card--front" aria-label="Card front">
  <div class="brand">
    <span class="brand__name">Meridian Civil<br>Supply</span>
  </div>
</section>

<section class="card card--back" aria-label="Card back">
  <svg class="wave" viewBox="0 0 760 434" aria-hidden="true">
    <path class="wave__stripe" d="M0 300 C 90 330, 200 350, 380 362 S 660 385, 760 434 L 0 434 Z"/>
    <path class="wave__gap" d="M0 312 C 90 342, 200 360, 380 371 S 660 392, 760 434 L 0 434 Z"/>
    <path class="wave__band" d="M0 320 C 90 352, 200 370, 380 380 S 650 398, 760 434 L 0 434 Z"/>
  </svg>

  <div class="brand">
    <span class="brand__name">Meridian Civil<br>Supply</span>
  </div>

  <div class="divider"></div>

  <div class="contact">
    <p class="contact__name">Reid Calloway</p>
    <p class="contact__title">Managing Director</p>
    <p class="contact__address">14 Wattle Row, Cedar Flats<br>QLD 4600, Australia</p>
    <p class="contact__line">
      <svg class="contact__icon" viewBox="0 0 24 24" aria-hidden="true"><path d="M6.6 10.8a15 15 0 0 0 6.6 6.6l2.2-2.2c.3-.3.7-.4 1-.2 1.1.4 2.3.6 3.6.6.6 0 1 .4 1 1V20c0 .6-.4 1-1 1A17 17 0 0 1 3 4c0-.6.4-1 1-1h3.5c.6 0 1 .4 1 1 0 1.3.2 2.5.6 3.6.1.3 0 .7-.2 1z"/></svg>
      +61 400 555 218 - AU
    </p>
    <p class="contact__line">
      <svg class="contact__icon" viewBox="0 0 24 24" aria-hidden="true"><path d="M7 1h10a2 2 0 0 1 2 2v18a2 2 0 0 1-2 2H7a2 2 0 0 1-2-2V3a2 2 0 0 1 2-2zm0 3v14h10V4zm5 15.5a1 1 0 1 0 0 2 1 1 0 0 0 0-2z"/></svg>
      +86 130 0555 4417 - CN
    </p>
    <p class="contact__line">
      <svg class="contact__icon" viewBox="0 0 24 24" aria-hidden="true"><path d="M2 5h20v14H2zm2 2v.5l8 5 8-5V7zm0 2.8V17h16V9.8l-8 5z"/></svg>
      reid@meridiancivil.com.au
    </p>
  </div>
</section>

</body>
</html>
```